2 Page Website in "wordpress"

We just bought rigadvisorhub.example and we need a 2 page website in wordpress coding. The top of the page should have a place to flash pictures of equipment examples that we consult on, selling or buying. "you can borrow pictures of all kinds of Dozers, Excavators, Backhoes, Mining Equipment from all over the Internet.

THE HOME PAGE
Then the first page needs to have 2 sections for general content, with links menu built in somewhere. We may add up to 10-15 links over time, so save some space for us. Then the 2nd page just needs to be a general contact form, for the buyer and seller. The 2 sections need to be set up for. 1.The buyer - Explanation - 2. For the Seller - Explanation -

THE FORM PAGE
There will be about 10 fields for general info so they can submit inquries, whether it is a seller contacting us to sell equipment, or a buyer wanting us to find them a specific piece of equipment. Just figure about 10 fields.

Logo
We need logo built in that represents equipment sales….

THIS MUST BE BUILT IN WORDPRESS CODE. It is our understanding that google is favoring websites built in wordpress.

Industry/Entity Type

Internet

Requirements
Must have
• Wordpress coded

```html
<!DOCTYPE html>
<html lang="en">
<head>
<meta charset="utf-8">
<title>RigAdvisor Hub</title>
<link href="https://fonts.googleapis.com/css2?family=Questrial&family=Open+Sans:wght@400;600&display=swap" rel="stylesheet">
<style>
  :root {
    --orange: #f39a12;
    --blue: #1e86e0;
    --blue-deep: #1268c9;
    --navy: #0f3c6e;
    --ink: #2a2a2a;
    --text: #666;
    --link: #2a6fc0;
    --footer-bg: #f3f3f3;
    --rule: #e6e6e6;
  }
  * { box-sizing: border-box; margin: 0; padding: 0; }
  html, body { width: 1200px; height: 1099px; overflow: hidden; background: #fff; }
  body { position: relative; font-family: "Open Sans", sans-serif; color: var(--text); }
  .abs { position: absolute; }

  .site-header { position: absolute; left: 0; top: 0; width: 1200px; height: 101px; background: #fff; }
  .brand { left: 152px; top: 30px; display: flex; align-items: center; gap: 10px;
    font-family: "Questrial", sans-serif; font-size: 28px; color: var(--orange); }
  .brand-mark { width: 26px; height: 26px; border-radius: 50%; background: var(--orange); }
  .main-nav { left: 606px; top: 42px; font-family: "Questrial", sans-serif; font-size: 18px; color: #555; }
  .main-nav a { position: absolute; white-space: nowrap; color: inherit; text-decoration: none; }

  .hero { left: 0; top: 101px; width: 1200px; height: 560px;
    background: linear-gradient(180deg, #2f7fd0 0%, #6aa8e3 35%, #cfe0ee 60%, #c9b190 72%, #b89a72 100%); }
  .hero-dots span { position: absolute; top: 628px; width: 14px; height: 14px; border-radius: 50%; background: #fff; }

  .inquiry { left: 744px; top: 232px; width: 294px; }
  .tab { position: absolute; top: 0; height: 40px; font-family: "Questrial", sans-serif; font-size: 16px;
    color: #fff; line-height: 40px; text-align: center; border-radius: 6px 6px 0 0; }
  .tab-buyer { left: 0; width: 142px; background: var(--blue); }
  .tab-seller { left: 144px; width: 138px; background: var(--orange); }
  .inquiry-body { position: absolute; left: 0; top: 40px; width: 294px; height: 286px;
    background: linear-gradient(180deg, var(--blue) 0%, var(--blue-deep) 100%); }
  .field { position: absolute; height: 32px; background: #fff; border: 1px solid #dfe6ee;
    font-size: 11.5px; color: #777; line-height: 30px; padding-left: 13px; }
  .submit { position: absolute; left: 28px; top: 229px; width: 118px; height: 33px; background: var(--navy);
    color: #fff; font-family: "Questrial", sans-serif; font-size: 16px; text-align: center; line-height: 33px; }

  .about-title { left: 151px; top: 720px; font-family: "Questrial", sans-serif; font-size: 30px; color: var(--ink); }
  .about-photo { left: 151px; top: 770px; width: 167px; height: 143px;
    background: linear-gradient(180deg, #5a9ad8 0%, #9cc1de 40%, #c7a84a 65%, #7da04a 100%); }
  .about-lead { left: 334px; top: 766px; width: 366px; font-size: 13.6px; line-height: 20px; color: #666; text-align: justify; }
  .about-body { left: 334px; top: 816px; width: 366px; font-size: 11.3px; line-height: 19.5px; color: #6a6a6a; text-align: justify; }
  .about-body p + p { margin-top: 2px; }

  .divider { left: 730px; top: 724px; width: 10px; height: 216px;
    background: linear-gradient(90deg, rgba(0,0,0,0.04), rgba(0,0,0,0)); }
  .resources-title { left: 782px; top: 726px; font-family: "Questrial", sans-serif; font-size: 23px; color: var(--orange); }
  .resources-intro { left: 782px; top: 760px; width: 260px; font-size: 11.5px; line-height: 19.5px; color: #6a6a6a; }
  .resource-links { left: 782px; top: 808px; width: 229px; list-style: none; }
  .resource-links li { height: 28.7px; border-bottom: 1px solid var(--rule); display: flex; align-items: center;
    gap: 9px; padding-left: 8px; font-size: 12.5px; color: var(--link); }
  .resource-links li:last-child { border-bottom: none; }

  .site-footer { left: 0; top: 994px; width: 1200px; height: 105px; background: var(--footer-bg); border-top: 1px solid #e8e8e8; }
  .footer-nav { left: 151px; top: 1020px; font-family: "Questrial", sans-serif; font-size: 15px; color: #555; word-spacing: 1px; }
  .copyright { left: 151px; top: 1050px; font-size: 11.5px; color: #666; }
  .social { top: 1023px; width: 24px; height: 24px; border-radius: 2px; }
  .social-a { left: 958px; background: #3b5a9a; }
  .social-b { left: 989px; background: #4fb5e6; }
  .social-c { left: 1020px; background: #1a6aa6; }
</style>
</head>
<body>
  <header class="site-header">
    <div class="abs brand"><span class="brand-mark"></span>RigAdvisor Hub</div>
    <nav class="abs main-nav">
      <a style="left:0">About Us</a>
      <a style="left:108px">Product</a>
      <a style="left:204px">Blog</a>
      <a style="left:275px">Reviews</a>
      <a style="left:373px">Contact</a>
    </nav>
  </header>

  <section class="abs hero" role="img" aria-label="Slideshow photo of an orange excavator with its bucket lowered on a gravel site under a blue cloudy sky"></section>
  <div class="hero-dots">
    <span style="left:557px"></span><span style="left:576px"></span><span style="left:595px"></span><span style="left:614px"></span>
  </div>

  <form class="abs inquiry">
    <div class="tab tab-buyer">Are you a Buyer</div>
    <div class="tab tab-seller">Are you a Seller</div>
    <div class="inquiry-body">
      <div class="field" style="left:24px;top:24px;width:238px">Full Name</div>
      <div class="field" style="left:24px;top:64px;width:238px">Phone no.</div>
      <div class="field" style="left:25px;top:105px;width:238px">Equipment needed</div>
      <div class="field" style="left:26px;top:144px;width:116px">Quantity</div>
      <div class="field" style="left:147px;top:144px;width:116px">Location</div>
      <div class="field" style="left:27px;top:185px;width:238px">Equipment needed</div>
      <div class="submit">SUBMIT</div>
    </div>
  </form>

  <h1 class="abs about-title">About Our Company &amp; Services</h1>
  <div class="abs about-photo" role="img" aria-label="Photo of a yellow wheel loader on a dirt site"></div>
  <p class="abs about-lead">Mauris vel lacus vitae felis vestibulum volutpat Etiam est nunc venenatis in tristique eu imperdiet</p>
  <div class="abs about-body">
    <p>ac nisl Cum sociis natoque penatibus et magnis dis parturient montes nascetur Ridiculus mus In iaculis facilisis massa Etiam eu urna Sed porta Suspendisse quam leo molestie</p>
    <p>sed luctus quis feugiat in pede Fusce tellus Sed metus augue convallis Curabitur iaculis tempus eros Curabitur</p>
  </div>

  <div class="abs divider"></div>
  <h2 class="abs resources-title">Resources &amp; Links</h2>
  <p class="abs resources-intro">Aique eu imperdiet ac nisl Cum sociis natoque penatibus et magnis dis parturient mo</p>
  <ul class="abs resource-links">
    <li><svg width="13" height="11" viewBox="0 0 13 11"><path d="M1 6 L5 10 L12 1" fill="none" stroke="#2a6fc0" stroke-width="2.4"/></svg>Why Choose Us</li>
    <li><svg width="13" height="11" viewBox="0 0 13 11"><path d="M1 6 L5 10 L12 1" fill="none" stroke="#2a6fc0" stroke-width="2.4"/></svg>Our Approach</li>
    <li><svg width="13" height="11" viewBox="0 0 13 11"><path d="M1 6 L5 10 L12 1" fill="none" stroke="#2a6fc0" stroke-width="2.4"/></svg>Services Provides</li>
    <li><svg width="13" height="11" viewBox="0 0 13 11"><path d="M1 6 L5 10 L12 1" fill="none" stroke="#2a6fc0" stroke-width="2.4"/></svg>Reviews &amp; Reports</li>
  </ul>

  <footer class="abs site-footer"></footer>
  <nav class="abs footer-nav">Home &nbsp;|&nbsp; About Us &nbsp;|&nbsp; Product &nbsp;|&nbsp; Blog &nbsp;|&nbsp; Reviews &nbsp;|&nbsp; Contact</nav>
  <p class="abs copyright">© 2014 Company Name &nbsp;All right reserved &nbsp;Term of Use</p>
  <span class="abs social social-a"></span>
  <span class="abs social social-b"></span>
  <span class="abs social social-c"></span>
</body>
</html>
```